Website for Swedish wellness company "Heartmeadow"

We need a website for our Swedish wellness company. The name is "Heartmeadow" . The company is all about sustainablility for our body, soul and planet. We work with coaching, yoga, massage, healthy food, retreats(sports, excercise, sufing), healing and inspirational talks. We are convinced that personal sustainability and a strong spiritual connection to yourself will lead to planetary sustainability. Our customers are both companies and consumers from all over the world. The final design should be clean/simple and you should get a feeling of community, happiness, warmth, connection,, joy, spirituality but still a professional touch.Just got a logo from Pixel Harbor and are very happy with it;-)
Updates

Sorry I was too enthusiastic posting this project. Of course I will give you some text as well för the different pages! I will see to that it is finished by friday so if you want to wait with your submissions please do! Best regards Maria

Target Market(s)

Businesses and consumers

Industry/Entity Type

Health And Wellness

Number of Pages Required

5+ page

Font styles to use
Sans Serif

Colors
33a6d7
00a990
b7a5cd

Requirements
Must have
• Idea about pages:
• I am not sure how many pages I get for the price, but 5 would be nice to start with.
• Not sure what write ups is;-)
• But title of the pages could be:
• Landing page
• About us
• Services
• Retreats
• Contact us
Nice to have
• A clean and professional website but with some heart and soul in it. Because we Would love colours that harmonize with our logo, but other ideas are welcome!

```html
<!DOCTYPE html>
<html lang="en">
<head>
<meta charset="utf-8">
<title>Heartmeadow – Wellness</title>
<link href="https://fonts.googleapis.com/css2?family=Dosis:wght@300;400;500;600;700&display=swap" rel="stylesheet">
<style>
:root{
  --navy:#10223d;
  --navy-deep:#0c1a30;
  --teal:#5fc9c6;
  --teal-dark:#3aa9a8;
  --ink:#1d2533;
  --text:#5a6270;
  --white:#ffffff;
  --social:#5b6675;
}
*{margin:0;padding:0;box-sizing:border-box}
html,body{width:1200px;height:3125px;overflow:hidden}
body{position:relative;background:var(--white);font-family:"Dosis",sans-serif;color:var(--ink)}
.section{position:absolute;left:0;width:1200px}
.photo{position:absolute}

/* nav */
.topbar{top:0;height:42px;background:var(--white)}
.social{position:absolute;left:231px;top:12px;display:flex;gap:14px}
.social span{width:17px;height:17px;background:var(--social);border-radius:3px}
.social span:nth-child(2),.social span:nth-child(4){border-radius:50%}
.nav{position:absolute;top:13px;left:602px;font-size:13px;font-weight:600;color:var(--ink)}
.nav a{color:inherit;text-decoration:none;position:absolute;white-space:nowrap}

/* hero */
.hero{top:42px;height:375px}
.hero-title{position:absolute;top:54px;font-size:31px;font-weight:500;color:var(--ink)}
.hero-title.light{color:var(--white)}
.logo-box{position:absolute;left:563px;top:100px;width:108px;height:87px;background:var(--white);display:flex;flex-direction:column;align-items:center;justify-content:center;gap:6px}
.logo-mark{width:26px;height:26px;border-radius:50%;background:var(--teal-dark)}
.logo-name{font-size:15px;font-weight:700;color:var(--navy);letter-spacing:.3px}
.slider-arrows{position:absolute;left:563px;top:248px;display:flex;gap:4px}
.slider-arrows span{width:34px;height:27px;display:flex;align-items:center;justify-content:center;background:rgba(95,201,198,.45);border:1px solid var(--teal)}
.slider-arrows span+span{background:var(--teal-dark)}

.btn-tab{position:absolute;display:flex;align-items:center;font-size:16px;font-weight:600;letter-spacing:3px;text-transform:uppercase}
.btn-tab::before{content:"";width:14px;height:30px;border-radius:15px 0 0 15px;background:var(--teal-dark);margin-right:-8px}
.btn-tab.on-dark{color:var(--white)}
.btn-tab.on-dark::before{background:#1b3f74}
.btn-tab.on-light{color:var(--ink)}

/* subscribe */
.subscribe{top:417px;height:79px;background:var(--navy)}
.subscribe h2{position:absolute;left:225px;top:22px;font-size:25px;font-weight:400;color:var(--teal)}
.subscribe h2 b{font-weight:700}
.sub-input{position:absolute;left:440px;top:23px;width:375px;height:33px;background:var(--white);font-size:11px;color:#8a93a0;padding:10px 12px}
.sub-btn{position:absolute;left:815px;top:23px;width:156px;height:33px;background:var(--teal);color:var(--navy);font-size:13px;font-weight:600;letter-spacing:3px;display:flex;align-items:center;justify-content:center}

/* headings */
.heading{position:absolute;display:flex;align-items:center;gap:10px;font-size:30px;font-weight:500;text-transform:uppercase;color:var(--ink)}
.heading.light{color:var(--white)}
.heading svg{width:12px;height:40px}
.copy{position:absolute;font-size:13px;line-height:20px;color:var(--text);font-weight:400}

/* about */
.about{top:496px;height:321px;background:var(--white)}

/* services */
.services{top:817px;height:404px}
.svc-panel{position:absolute;left:225px;top:110px;width:421px;height:292px;background:rgba(12,26,48,.75)}
.svc-item{position:absolute;left:0;display:flex;align-items:flex-start}
.svc-icon{width:44px;height:44px;margin-left:18px;border:2px solid var(--teal);border-radius:50%}
.svc-divider{width:1px;height:50px;background:rgba(255,255,255,.3);margin:0 20px 0 24px;transform:skewX(-20deg)}
.svc-item h3{font-size:16px;font-weight:700;color:var(--white);margin-bottom:10px}
.svc-item p{font-size:10px;line-height:13px;color:#b9c3d0;width:300px}

/* retreats */
.retreats{top:1221px;height:400px;background:var(--white)}

/* gallery */
.gallery{top:1621px;height:558px}
.filters{position:absolute;left:229px;top:125px;width:746px;height:39px;border-radius:20px;background:#c9d1db;font-size:11px;font-weight:600;color:var(--navy)}
.filters span{position:absolute;top:13px;white-space:nowrap}
.filters .active{left:12px;top:5px;height:29px;width:130px;border-radius:15px;background:#29507f;color:var(--white);display:flex;align-items:center;justify-content:center}
.tile{position:absolute;overflow:hidden}
.tile .tag{position:absolute;left:12px;bottom:10px;font-size:17px;font-weight:500;color:var(--teal);line-height:19px}
.tile-note{position:absolute;left:12px;font-size:9px;line-height:12px;color:#e3e8ee;width:150px}

/* healthy foods */
.foods{top:2179px;height:390px;background:var(--white)}
.subtitle{position:absolute;font-size:20px;font-weight:500;color:var(--teal-dark)}

/* contact */
.contact{top:2569px;height:354px}
.contact-panel{position:absolute;left:0;top:0;width:600px;height:354px;background:var(--navy)}
.contact-item{position:absolute;left:225px;display:flex;align-items:center;gap:15px;font-size:18px;color:var(--white);letter-spacing:.5px}
.c-icon{width:31px;height:42px;border-radius:8px;background:var(--teal);display:flex;align-items:center;justify-content:center}

/* footer */
.footer{top:2923px;height:202px;background:var(--white)}
.footer-logo{position:absolute;left:0;width:1200px;top:50px;display:flex;flex-direction:column;align-items:center;gap:8px}
.footer-logo .logo-mark{width:40px;height:40px}
.footer-logo .logo-name{font-size:20px}
.copyright{position:absolute;left:0;width:1200px;top:173px;text-align:center;font-size:12px;font-weight:600;color:var(--ink);letter-spacing:.8px}
</style>
</head>
<body>

<header class="section topbar">
  <div class="social" aria-label="Social links"><span></span><span></span><span></span><span></span></div>
  <nav class="nav">
    <a style="left:0">Home</a>
    <a style="left:60px">About us</a>
    <a style="left:140px">Services</a>
    <a style="left:219px">Retreats</a>
    <a style="left:296px">Contact us</a>
  </nav>
</header>

<section class="section hero">
  <div class="photo" role="img" aria-label="Smiling woman holding a plank on a sunny beach" style="left:0;top:0;width:600px;height:375px;background:linear-gradient(180deg,rgba(236,232,226,0) 55%,#d8cdbd 100%),radial-gradient(ellipse at 55% 55%,#c7a88e 0%,rgba(199,168,142,0) 35%),linear-gradient(100deg,#e9e5df 0%,#dcd4c9 40%,#cdbda9 70%,#ecebe8 100%)"></div>
  <div class="photo" role="img" aria-label="Athletic woman resting on the floor after exercise in a dark studio" style="left:600px;top:0;width:600px;height:375px;background:radial-gradient(ellipse at 70% 30%,#5a5150 0%,rgba(40,38,40,0) 40%),radial-gradient(ellipse at 55% 50%,#333335 0%,#1a1a1c 55%,#0a0a0b 100%)"></div>
  <h1 class="hero-title" style="left:225px">Yoga Training</h1>
  <h2 class="hero-title light" style="left:637px">Excercise</h2>
  <div class="logo-box"><span class="logo-mark"></span><span class="logo-name">HEARTMEADOW</span></div>
  <div class="slider-arrows">
    <span><svg width="10" height="12" viewBox="0 0 10 12"><path d="M8 1L2 6l6 5" fill="none" stroke="#10223d" stroke-width="1.6"/></svg></span>
    <span><svg width="10" height="12" viewBox="0 0 10 12"><path d="M2 1l6 5-6 5" fill="none" stroke="#10223d" stroke-width="1.6"/></svg></span>
  </div>
  <a class="btn-tab on-light" style="left:225px;top:320px">Register Now</a>
  <a class="btn-tab on-dark" style="left:650px;top:320px">Register Now</a>
</section>

<section class="section subscribe">
  <h2><b>Subscribe</b> Here Now</h2>
  <div class="sub-input">Enter Your Email address</div>
  <div class="sub-btn">SUBSCRIBE</div>
</section>

<section class="section about">
  <div class="photo" role="img" aria-label="Therapist giving a massage to a guest at an outdoor spa" style="left:0;top:0;width:448px;height:321px;background:radial-gradient(ellipse at 65% 45%,#3b3b3d 0%,rgba(59,59,61,0) 28%),linear-gradient(180deg,rgba(255,255,255,0) 70%,#cfc6ba 100%),linear-gradient(90deg,#8f918d 0%,#c3bdb2 40%,#e4e0d9 75%,#ffffff 100%)"></div>
  <h2 class="heading" style="left:462px;top:40px">
    <svg viewBox="0 0 12 40"><path d="M2 2Q12 20 2 38" fill="none" stroke="#5fc9c6" stroke-width="1.6"/></svg>About us<svg viewBox="0 0 12 40"><path d="M10 2Q0 20 10 38" fill="none" stroke="#5fc9c6" stroke-width="1.6"/></svg>
  </h2>
  <p class="copy" style="left:465px;top:114px;width:506px">Lorem Ipsum is simply dummy text of the printing and typesetting industry. Lorem Ipsum has been the industry's standard dummy text ever since the 1500s, when an unknown printer took a galley of type and scrambled it to make a type specimen book. It has survived not only five centuries, but also the leap into electronic typesetting, remaining essentially unchanged. It was popularised in the 1960s with the release.</p>
  <a class="btn-tab on-light" style="left:465px;top:239px">Read More</a>
</section>

<section class="section services">
  <div class="photo" role="img" aria-label="Group of women stretching in a yoga class inside a large loft studio" style="left:0;top:0;width:1200px;height:404px;background:radial-gradient(ellipse at 75% 80%,#e9e6e3 0%,rgba(233,230,227,0) 18%),linear-gradient(90deg,#16284a 0%,#1c3050 40%,#243a5c 65%,#1e3354 85%,#17294a 100%)"></div>
  <h2 class="heading light" style="left:230px;top:42px">
    <svg viewBox="0 0 12 40"><path d="M2 2Q12 20 2 38" fill="none" stroke="#5fc9c6" stroke-width="1.6"/></svg>Services<svg viewBox="0 0 12 40"><path d="M10 2Q0 20 10 38" fill="none" stroke="#5fc9c6" stroke-width="1.6"/></svg>
  </h2>
  <div class="svc-panel">
    <div class="svc-item" style="top:24px"><span class="svc-icon"></span><span class="svc-divider"></span><div><h3>Coaching</h3><p>Lorem Ipsum is simply dummy text of the printing and typesetting industry. Lorem Ipsum has been the industry's standard</p></div></div>
    <div class="svc-item" style="top:128px"><span class="svc-icon"></span><span class="svc-divider"></span><div><h3>Yoga</h3><p>Lorem Ipsum is simply dummy text of the printing and typesetting industry. Lorem Ipsum has been the industry's standard</p></div></div>
    <a class="btn-tab on-dark" style="left:0;top:240px;color:var(--teal);font-weight:500">View All Services</a>
  </div>
</section>

<section class="section retreats">
  <div class="photo" role="img" aria-label="Woman meditating with hands pressed together above her head" style="left:225px;top:45px;width:244px;height:355px;background:radial-gradient(ellipse at 50% 45%,#c9a58c 0%,rgba(201,165,140,0) 30%),linear-gradient(180deg,#ffffff 0%,#eeebe8 40%,#d9d6d4 75%,#f2f2f3 100%)"></div>
  <h2 class="heading" style="left:483px;top:115px">
    <svg viewBox="0 0 12 40"><path d="M2 2Q12 20 2 38" fill="none" stroke="#5fc9c6" stroke-width="1.6"/></svg>Retreats<svg viewBox="0 0 12 40"><path d="M10 2Q0 20 10 38" fill="none" stroke="#5fc9c6" stroke-width="1.6"/></svg>
  </h2>
  <p class="copy" style="left:494px;top:195px;width:477px">Lorem Ipsum is simply dummy text of the printing and typesetting industry. Lorem Ipsum has been the industry's standard dummy text ever since the 1500s, when an unknown printer took a galley of type and scrambled it to make a type specimen book. It has survived not only five centuries, but also the leap into electronic typesetting, remaining essentially unchanged. It was popularised in the 1960s with the release.</p>
  <a class="btn-tab on-light" style="left:494px;top:316px">Read More</a>
</section>

<section class="section gallery">
  <div class="photo" role="img" aria-label="Dim gym interior with people training, darkened behind the gallery" style="left:0;top:0;width:1200px;height:558px;background:linear-gradient(90deg,#1a2a44 0%,#22355a 45%,#1e3050 70%,#15243d 100%)"></div>
  <h2 class="heading light" style="left:0;width:1200px;justify-content:center;top:50px">
    <svg viewBox="0 0 12 40"><path d="M2 2Q12 20 2 38" fill="none" stroke="#5fc9c6" stroke-width="1.6"/></svg>Our Gallery<svg viewBox="0 0 12 40"><path d="M10 2Q0 20 10 38" fill="none" stroke="#5fc9c6" stroke-width="1.6"/></svg>
  </h2>
  <div class="filters">
    <span class="active">All Categories</span>
    <span style="left:162px">Training</span>
    <span style="left:254px">Yoga</span>
    <span style="left:330px">Exercies</span>
    <span style="left:424px">Inspirational Events</span>
    <span style="left:573px">Message</span>
    <span style="left:667px">Healthy Food</span>
  </div>

  <div class="tile" role="img" aria-label="Woman in a yoga headstand at sunset" style="left:223px;top:185px;width:187px;height:263px;background:linear-gradient(180deg,#c9a070 0%,#8e6d55 45%,#3f3a3c 100%)">
    <span class="tag" style="bottom:90px">#Yoga</span>
    <p class="tile-note" style="top:185px">Lorem Ipsum is simply dummy text of the printing and typesetting industry.</p>
    <span class="tag" style="bottom:20px;font-size:12px;letter-spacing:1px">See Now</span>
  </div>
  <div class="tile" role="img" aria-label="Gym class training with weights" style="left:423px;top:185px;width:169px;height:127px;background:linear-gradient(160deg,#4a3d35 0%,#1d1b1c 100%)"><span class="tag">#Training</span></div>
  <div class="tile" role="img" aria-label="Speaker on stage at an inspirational event" style="left:423px;top:323px;width:169px;height:125px;background:radial-gradient(ellipse at 50% 30%,#5a4640 0%,#151517 80%)"><span class="tag">#Inspirational<br>Events</span></div>
  <div class="tile" role="img" aria-label="People exercising in a crowded gym" style="left:606px;top:185px;width:188px;height:263px;background:radial-gradient(ellipse at 85% 10%,#b33a3a 0%,rgba(179,58,58,0) 25%),linear-gradient(170deg,#5a4a48 0%,#35302f 50%,#202022 100%)"><span class="tag">#Exercise</span></div>
  <div class="tile" role="img" aria-label="Relaxing back massage" style="left:806px;top:185px;width:169px;height:127px;background:linear-gradient(160deg,#e7b488 0%,#c47b45 60%,#8a4b2a 100%)"><span class="tag">#Message</span></div>
  <div class="tile" role="img" aria-label="Fresh red berries" style="left:806px;top:323px;width:169px;height:125px;background:radial-gradient(circle at 40% 40%,#d43a3e 0%,#9a1c24 60%,#5a0e14 100%)"><span class="tag">#Healthy Foods</span></div>

  <a class="btn-tab on-dark" style="left:540px;top:476px;color:var(--teal);font-weight:500">View More</a>
</section>

<section class="section foods">
  <div class="photo" role="img" aria-label="Salad bowl, vegetables, skipping rope and water bottle on a wooden table" style="left:0;top:0;width:583px;height:390px;background:radial-gradient(circle at 55% 45%,#e8eae6 0%,rgba(232,234,230,0) 16%),radial-gradient(ellipse at 12% 30%,#d06a3a 0%,rgba(208,106,58,0) 18%),linear-gradient(120deg,#9a7a5c 0%,#b99878 35%,#5f6a78 70%,#3e4a5a 100%)"></div>
  <h2 class="heading" style="left:596px;top:67px">
    <svg viewBox="0 0 12 40"><path d="M2 2Q12 20 2 38" fill="none" stroke="#5fc9c6" stroke-width="1.6"/></svg>Healthy Foods<svg viewBox="0 0 12 40"><path d="M10 2Q0 20 10 38" fill="none" stroke="#5fc9c6" stroke-width="1.6"/></svg>
  </h2>
  <p class="subtitle" style="left:600px;top:131px">We Also Prefer Heathy Foods</p>
  <p class="copy" style="left:600px;top:185px;width:372px">Lorem Ipsum is simply dummy text of the printing and typesetting industry. Lorem Ipsum has been the industry's standard dummy text ever since the 1500s, when an unknown printer took a galley of type and scrambled it to make a type</p>
  <a class="btn-tab on-light" style="left:600px;top:293px">Read More</a>
</section>

<section class="section contact">
  <div class="contact-panel"></div>
  <div class="photo" role="img" aria-label="Black and white close-up of a waist being measured with a tape" style="left:600px;top:0;width:600px;height:354px;background:linear-gradient(110deg,#f4f4f4 0%,#d6d6d6 35%,#9c9c9c 60%,#e4e4e4 100%)"></div>
  <h2 class="heading light" style="left:230px;top:34px">
    <svg viewBox="0 0 12 40"><path d="M2 2Q12 20 2 38" fill="none" stroke="#5fc9c6" stroke-width="1.6"/></svg>Contact us<svg viewBox="0 0 12 40"><path d="M10 2Q0 20 10 38" fill="none" stroke="#5fc9c6" stroke-width="1.6"/></svg>
  </h2>
  <div class="contact-item" style="top:127px">
    <span class="c-icon"><svg width="14" height="22" viewBox="0 0 14 22"><rect x="1" y="1" width="12" height="20" rx="2" fill="none" stroke="#10223d" stroke-width="1.8"/><line x1="5" y1="17.5" x2="9" y2="17.5" stroke="#10223d" stroke-width="1.8"/></svg></span>
    +46-5550192834
  </div>
  <div class="contact-item" style="top:193px">
    <span class="c-icon"><svg width="10" height="22" viewBox="0 0 10 22"><circle cx="5.5" cy="3" r="2.6" fill="#10223d"/><path d="M2 9h5v10h2v2H1v-2h2v-8H2z" fill="#10223d"/></svg></span>
    www.heartmeadow@info.mail.com
  </div>
  <div class="contact-item" style="top:262px">
    <span class="c-icon"><svg width="16" height="22" viewBox="0 0 16 22"><path d="M8 1C4.1 1 1 4.1 1 8c0 5 7 13 7 13s7-8 7-13c0-3.9-3.1-7-7-7z" fill="#10223d"/><circle cx="8" cy="8" r="2.6" fill="#5fc9c6"/></svg></span>
    Alder Valley, USA
  </div>
</section>

<footer class="section footer">
  <div class="footer-logo"><span class="logo-mark"></span><span class="logo-name">HEARTMEADOW</span></div>
  <p class="copyright">All Copyright Reserved 2019 &nbsp;|&nbsp; Heartmeadow Private Ltd.</p>
</footer>

</body>
</html>
```